Adult Job Portal needs a Web Design

We need a web design for a landing and search page for an ADULT-JOB-portal.

The structure of landing page can be taken from zestmingle.com.

The structure of job search page can be taken from: http://www.careersinfenbury.co.uk/

Users should be able to recognize that is a SEX-INDUSTRY job portal.

The project name can not be published for ... some reasons.
Updates

Hi, Hivelings.

Please note: the project was upgraded to "Guaranteed"
Thanks in advance for great work.
BR. M.

Hi ArtHivelings,
please find attached the landing page wireframe.
It should make it easier for you to know what is expected.
Thanks in advance, guys!

Target Market(s)

women 18 to 30 years old

Industry/Entity Type

Adult

Requirements
Must have
• We expect to get design for the following pages:
- Landing page
- Add profile (name, description, photos, skills, preferable location)
- Job search with filters (example http://www.careersinfenbury.co.uk/jobs)
- Companies list (example http://www.careersinfenbury.co.uk/companies-in-fenbury)
- Company page (example http://www.careersinfenbury.co.uk/company/pelvoro)
Should not have
• pornography, violence

```html
<!DOCTYPE html>
<html lang="en">
<head>
<meta charset="utf-8">
<title>Adult Job Portal – Landing</title>
<link rel="stylesheet" href="https://fonts.googleapis.com/css2?family=Open+Sans:wght@400;600;700&family=Roboto+Condensed:wght@400;700&family=Noto+Serif:ital@1&display=swap">
<style>
  :root{
    --plum-dark:#2a1228;
    --plum:#6b0f55;
    --pink:#ec168f;
    --pink-light:#f34aa8;
    --white:#ffffff;
    --grey-icon:#a7a6aa;
    --grey-ring:#e2e1e3;
    --text:#1a1a1a;
    --footer-text:#6a2a62;
  }
  *{margin:0;padding:0;box-sizing:border-box}
  html,body{width:1200px;height:900px;overflow:hidden;background:var(--white)}
  body{position:relative;font-family:"Open Sans",Arial,sans-serif;color:var(--text)}

  .topbar{position:absolute;left:0;top:0;width:1200px;height:36px;background:var(--plum-dark)}
  .audience-links{position:absolute;right:106px;top:9px;display:flex;gap:11px}
  .audience-links a{display:block;background:#5a1450;color:var(--white);font-size:12px;line-height:18px;padding:0 12px;text-decoration:none}

  .navbar{position:absolute;left:0;top:36px;width:1200px;height:75px;
    background:linear-gradient(to bottom,#f04a9f 0%,var(--pink) 45%,#e0147f 60%,#f25aa8 100%)}
  .main-nav{position:absolute;left:355px;top:0;display:flex;height:75px}
  .main-nav a{color:var(--white);text-decoration:none;font-size:14px;line-height:75px;padding:0 14.5px}
  .main-nav a.active{background:linear-gradient(to bottom,#f56bb3,#e81c8a);padding:0 16px;border-left:1px solid #f88cc4;border-right:1px solid #f88cc4}

  .brand{position:absolute;left:105px;top:0;width:200px;height:124px;z-index:3}
  .brand-name{position:absolute;left:90px;top:14px;font-size:30px;font-weight:700;line-height:32px;color:var(--plum)}

  .hero{position:absolute;left:0;top:111px;width:1200px;height:446px;
    background:linear-gradient(100deg,#b9bbbe 0%,#8d8c90 25%,#c6a79a 45%,#6f6e72 60%,#cfd0d3 80%,#e3e4e6 100%)}
  .hero-title{position:absolute;left:104px;top:34px;font-family:"Roboto Condensed","Arial Narrow",sans-serif;font-weight:700;font-size:50px;color:var(--white);letter-spacing:-0.5px;line-height:60px}
  .hero-copy{position:absolute;left:103px;top:96px;width:416px;height:130px;background:rgba(255,255,255,0.45);padding:6px 10px;font-size:13px;line-height:24px;color:#111}
  .hero-copy em{font-style:normal;color:var(--pink)}
  .btn{position:absolute;top:245px;height:46px;color:var(--white);font-family:"Roboto Condensed","Arial Narrow",sans-serif;font-size:25px;line-height:46px;text-align:center;text-decoration:none}
  .btn-info{left:103px;width:198px;background:linear-gradient(to bottom,#7b1a66,#4e0b3f)}
  .btn-subscribe{left:322px;width:138px;background:linear-gradient(to bottom,#f13a9c,#d70f7e)}
  .slider-arrow{position:absolute;top:212px;width:36px;height:33px;background:linear-gradient(#ffffff,#dcdcdc);border:1px solid #bbb}
  .slider-arrow.prev{left:37px}
  .slider-arrow.next{left:1128px}

  .features{position:absolute;left:0;top:557px;width:1200px;height:273px;display:flex;justify-content:center}
  .feature{position:relative;width:379px;text-align:center}
  .feature + .feature::before{content:"";position:absolute;left:0;top:28px;height:220px;border-left:1px solid #d6d6d6}
  .feature-icon{display:block;margin:13px auto 0}
  .feature h2{font-family:"Noto Serif",Georgia,serif;font-style:italic;font-weight:400;font-size:21px;margin-top:14px;line-height:28px}
  .feature p{font-size:13px;line-height:20px;margin:7px auto 0;width:265px}

  .footer{position:absolute;left:0;top:830px;width:1200px;height:70px;background:var(--plum-dark);border-top:2px solid #fff;box-shadow:0 -1px 0 #7d6d7b}
  .social{position:absolute;left:535px;top:10px;display:flex;gap:9px}
  .copyright{position:absolute;left:0;top:49px;width:1200px;text-align:center;font-size:12px;color:var(--footer-text)}
</style>
</head>
<body>
  <header>
    <div class="topbar">
      <nav class="audience-links"><a href="#">For Girls</a><a href="#">For Clubs</a></nav>
    </div>
    <div class="navbar">
      <nav class="main-nav">
        <a class="active" href="#">Home</a>
        <a href="#">For Him</a>
        <a href="#">For Her</a>
        <a href="#">Man Jone</a>
        <a href="#">Sex Essentials</a>
        <a href="#">Ladies Night</a>
        <a href="#">Clearence</a>
        <a href="#">Contact Us</a>
      </nav>
    </div>
    <div class="brand">
      <svg width="200" height="124" viewBox="0 0 200 124">
        <defs><linearGradient id="brandPanel" x1="0" y1="0" x2="0" y2="1"><stop offset="0" stop-color="#ffffff"/><stop offset="1" stop-color="#e6e6e6"/></linearGradient></defs>
        <path d="M0 0H200V92L100 124L0 92Z" fill="url(#brandPanel)"/>
        <circle cx="43" cy="47" r="34" fill="none" stroke="#6b0f55" stroke-width="3"/>
      </svg>
      <span class="brand-name">Logo<br>Here</span>
    </div>
  </header>

  <section class="hero" role="img" aria-label="Photo of a model in lingerie lying on a bed, with two smartphones showing the mobile version of the site">
    <h1 class="hero-title">Find your next job!</h1>
    <p class="hero-copy">Cum sociis natoque palesuada odio. Morbi nunc odio, gravida at, cursus nec, luctus a, lorem. Maecenas tristique orci ac sem. Duis ultricies pharetoem ipsum dolor sit amet, consect etuer adienat ibus et magnis dis parturient montes, nascetur ridiculus mus <em>feugiat malesuada!</em></p>
    <a class="btn btn-info" href="#">More Information</a>
    <a class="btn btn-subscribe" href="#">Subscribe</a>
    <span class="slider-arrow prev"><svg width="34" height="31" viewBox="0 0 34 31"><path d="M21 8L13 15.5L21 23" fill="none" stroke="#222" stroke-width="4"/></svg></span>
    <span class="slider-arrow next"><svg width="34" height="31" viewBox="0 0 34 31"><path d="M13 8L21 15.5L13 23" fill="none" stroke="#222" stroke-width="4"/></svg></span>
  </section>

  <main class="features">
    <article class="feature">
      <svg class="feature-icon" width="114" height="114" viewBox="0 0 114 114">
        <circle cx="57" cy="57" r="54" fill="#6b0f55" stroke="#ec168f" stroke-width="5"/>
        <circle cx="52" cy="52" r="17" fill="none" stroke="#fff" stroke-width="6"/>
        <path d="M64 64L80 80" stroke="#fff" stroke-width="9" stroke-linecap="round"/>
      </svg>
      <h2>Find</h2>
      <p>Maecenas tristique orci ac sem. Duis ultri­cies phar istietra arbunc odio, gravida at, cunas tristique orci acm. Duis ultricies pharsan malesuada orci.</p>
    </article>
    <article class="feature">
      <svg class="feature-icon" width="114" height="114" viewBox="0 0 114 114">
        <circle cx="57" cy="57" r="54" fill="#a7a6aa" stroke="#e2e1e3" stroke-width="5"/>
        <path d="M34 58L50 73L80 44" fill="none" stroke="#fff" stroke-width="11" stroke-linecap="round" stroke-linejoin="round"/>
      </svg>
      <h2>Apply</h2>
      <p>Maecenas tristique orci ac sem. Duis ultri­cies phar istietra arbunc odio, gravida at, cunas tristique orci acm. Duis ultricies pharsan malesuada orci.</p>
    </article>
    <article class="feature">
      <svg class="feature-icon" width="114" height="114" viewBox="0 0 114 114">
        <circle cx="57" cy="57" r="54" fill="#a7a6aa" stroke="#e2e1e3" stroke-width="5"/>
        <g fill="#fff">
          <path d="M57 32L67 44H47Z"/><path d="M57 82L67 70H47Z"/>
          <path d="M32 57L44 47V67Z"/><path d="M82 57L70 47V67Z"/>
          <rect x="52" y="42" width="10" height="30"/><rect x="42" y="52" width="30" height="10"/>
        </g>
      </svg>
      <h2>Move</h2>
      <p>Maecenas tristique orci ac sem. Duis ultri­cies phar istietra arbunc odio, gravida at, cunas tristique orci acm. Duis ultricies pharsan malesuada orci.</p>
    </article>
  </main>

  <footer class="footer">
    <div class="social">
      <svg width="32" height="32" viewBox="0 0 32 32"><circle cx="16" cy="16" r="14.5" fill="#4e0b3f" stroke="#fff" stroke-width="1.5"/></svg>
      <svg width="32" height="32" viewBox="0 0 32 32"><circle cx="16" cy="16" r="14.5" fill="#4e0b3f" stroke="#fff" stroke-width="1.5"/></svg>
      <svg width="32" height="32" viewBox="0 0 32 32"><circle cx="16" cy="16" r="14.5" fill="#4e0b3f" stroke="#fff" stroke-width="1.5"/></svg>
    </div>
    <p class="copyright">© Copyright 2013 velvetshift.com. All Rights Reserved</p>
  </footer>
</body>
</html>
```